PowerPoint design of key models

We recently had a new PPT template created which we are very happy with. Now we want to have some of our key models on various pages in PPT to be reformatted and redesigned to match the other graphics of the new PT template. Can you please redesign the models and graphics so they have the same look and feel as the new template. I have included both files for you to work with. Thank you.

```html
<!DOCTYPE html>
<html lang="en">
<head>
<meta charset="utf-8">
<title>Key Models – Slide Set</title>
<link href="https://fonts.googleapis.com/css2?family=Open+Sans:ital,wght@0,400;0,600;0,700;1,400;1,600&family=Ubuntu:wght@500;700&display=swap" rel="stylesheet">
<style>
:root{
  --navy:#232a63;
  --blue:#1a6fc2;
  --sky:#2aa8e0;
  --link:#2f8fd8;
  --lavender:#d3d6ec;
  --grey:#efefef;
  --grey2:#e4e4e4;
  --ink:#222;
  --muted:#8a8a8a;
  --divider:#2f8fd8;
}
*{box-sizing:border-box;margin:0;padding:0}
html,body{width:1200px;height:847px;overflow:hidden;background:#fff}
body{font-family:"Open Sans",sans-serif;color:var(--ink)}
.sheet{display:grid;grid-template-columns:396px 407px 397px;grid-template-rows:288px 290px 269px;width:1200px;height:847px}
.slide{position:relative;overflow:hidden;border-right:1px solid var(--divider);border-bottom:1px solid var(--divider)}
.slide:nth-child(3n){border-right:none}
.slide:nth-child(n+7){border-bottom:none}
.title{position:absolute;font-family:"Ubuntu",sans-serif;font-weight:500;color:#111;font-size:15px;white-space:nowrap;display:flex;align-items:center}
.title::before{content:"";display:inline-block;width:17px;height:3px;margin-right:7px;background:linear-gradient(90deg,var(--sky),var(--blue))}
.brand{position:absolute;top:13px;right:12px;display:flex;align-items:center;gap:3px;font-size:6.3px;font-weight:600;color:var(--navy)}
.brand .dot{width:9px;height:9px;border-radius:50%;background:var(--blue)}
.footer{position:absolute;left:18px;right:10px;bottom:var(--fb,18px);height:9px;display:flex;align-items:center}
.footer .url{font-size:4.3px;color:#333;width:55px}
.footer .band{flex:1;height:9px;background:linear-gradient(90deg,var(--sky),var(--blue));clip-path:polygon(2% 0,100% 0,99% 100%,0 100%);display:flex;align-items:center;justify-content:center;font-size:3.4px;color:#d9ecfa}
.footer .page{width:20px;height:9px;margin-left:4px;background:var(--navy);clip-path:polygon(15% 0,100% 0,85% 100%,0 100%);color:#fff;font-size:5px;font-weight:700;display:flex;align-items:center;justify-content:center}
.row2{--fb:16px}.row3{--fb:10px}

/* FAB */
.fab{position:absolute;left:20px;top:50px;width:358px}
.fab-row{display:flex;margin-bottom:1px}
.fab-row .term{width:104px;background:var(--navy);color:#fff;font-family:"Ubuntu",sans-serif;font-weight:500;font-size:14px;display:flex;align-items:center;padding-left:18px}
.fab-row .def{flex:1;font-size:8.6px;line-height:1.4;padding:5px 4px}
.fab-row .def u{color:var(--link);font-weight:600}
.fab-row:nth-child(odd) .def{background:var(--grey)}
.fab-row:nth-child(even) .def{background:var(--lavender)}

/* needs */
.intro{position:absolute;left:20px;right:20px;top:48px;text-align:center;font-size:8.6px;line-height:1.4}
.grid-table{position:absolute;border-collapse:separate;border-spacing:1px;table-layout:fixed}
.grid-table th{background:var(--navy);color:#fff;font-weight:600;text-align:left}
.needs{left:28px;top:103px;width:358px;font-size:7px}
.needs th{height:23px;padding:0 3px;font-size:7.4px;vertical-align:top;padding-top:3px}
.needs td{height:12.5px;padding:0 3px;background:#fff}
.needs tr:nth-child(odd) td{background:var(--grey)}
.needs .gap td{background:#fff;height:11px}
.needs .blank td{background:var(--grey2)}

/* HPBD */
.hp{position:absolute;left:25px;top:65px;width:359px;display:grid;grid-template-columns:1fr 1fr;gap:0 1px}
.hp .head{background:var(--navy);color:#fff;font-size:7.8px;font-weight:600;text-align:center;height:15px;line-height:15px;border-bottom:1px solid #6c7ab8}
.hp .area{background:var(--grey2);height:82px}
.hp .area.tall{height:72px}

/* strategic */
.sub{position:absolute;font-size:8px}
.strat{left:23px;top:67px;width:352px;font-size:7px}
.strat th{height:15px;padding:0 3px;font-size:7px}
.strat td{height:22px}
.strat td.dim{background:var(--blue)}
.strat tr:nth-child(even) td:not(.dim){background:var(--grey)}
.strat tr:nth-child(odd) td:not(.dim){background:var(--grey2)}

/* objections */
.obj{left:29px;top:54px;width:352px;font-size:7px}
.obj th{height:26px;padding:0 4px;font-size:9px}
.obj td{height:33px;padding:0 4px;background:var(--grey);line-height:1.35}
.obj td.type{font-weight:700;color:var(--navy);font-size:7.6px}

/* SPACER */
.spacer-sub{position:absolute;left:25px;top:57px;font-size:8.6px;color:var(--blue)}
.spacer-sub b{font-weight:700;color:var(--navy)}
.spacer{position:absolute;left:21px;top:74px;width:344px}
.spacer .item{display:flex;height:30.5px;margin-bottom:1px}
.spacer .word{width:64px;background:var(--navy);color:#fff;font-family:"Ubuntu",sans-serif;font-weight:500;font-size:9.6px;display:flex;align-items:center;padding-left:4px}
.spacer .word b{font-size:11.5px}
.spacer .text{flex:1;background:var(--grey);font-size:6.8px;line-height:1.35;padding:0 5px;display:flex;align-items:center}

/* behaviours */
.beh{left:29px;top:51px;width:341px;font-size:3.6px;line-height:1.45}
.beh th{height:13px;text-align:center;font-size:4.2px}
.beh td{background:var(--grey);vertical-align:top;padding:3px}
.beh td.obj-cell{padding:3px}
.beh td.prac{font-weight:700;font-size:3.8px}
.beh ul{padding-left:8px}

/* opportunity matrix */
.axis{position:absolute;font-size:8px;font-weight:600}
.axis.on{color:var(--blue)}
.axis.off{color:var(--muted);font-weight:400}
.matrix{position:absolute;left:96px;top:63px;width:286px;height:182px;border:1px solid var(--navy);display:grid;grid-template-columns:1fr 1fr;grid-template-rows:1fr 1fr}
.quad{position:relative;border-right:1px solid var(--navy);font-size:6px;line-height:1.4}
.quad:nth-child(even){border-right:none}
.quad h4{background:var(--navy);color:#fff;font-weight:400;font-size:6.2px;padding:2px 3px;line-height:1.4}
.quad p{font-weight:600;padding:3px 3px 2px}
.quad ul{list-style:none;padding-left:8px}
.quad li::before{content:"▪";color:var(--sky);margin-right:4px;font-size:5px}
.zig{position:absolute;left:209px;top:137px}

/* GROW */
.grow-shape{position:absolute;left:25px;top:53px}
.grow-label{position:absolute;font-size:5px;line-height:1.5}
.col{position:absolute;font-size:4.2px;line-height:1.45}
.col .block{background:var(--grey);padding:2px 3px;margin-bottom:2px}
.col h5{font-size:5.4px;font-weight:700;margin-bottom:2px}
.col ol,.col ul{padding-left:8px}
.col li{margin-bottom:1px}
.col .q li{list-style:none}
.col .q li::before{content:"☐ ";color:var(--blue)}
.col .lead{font-weight:700;font-style:italic}
</style>
</head>
<body>
<main class="sheet">

<!-- 14 -->
<section class="slide">
  <h2 class="title" style="left:23px;top:22px">Features, Advantages &amp; Benefits</h2>
  <div class="brand"><span class="dot"></span>Summit Advisory</div>
  <div class="fab">
    <div class="fab-row" style="height:47px"><div class="term">Feature</div><div class="def"><u>What</u> it is or has in the product/service itself<br>- An <b>indisputable characteristic or attribute</b></div></div>
    <div class="fab-row" style="height:43px"><div class="term">Advantage</div><div class="def"><u>How</u> the feature works<br>- what it <b>does, or doesn't do</b></div></div>
    <div class="fab-row" style="height:43px"><div class="term">Benefit</div><div class="def"><u>Why</u> they should buy it<br>- The <b>end result or outcome</b> for people or businesses</div></div>
    <div class="fab-row" style="height:50px"><div class="term">Proof</div><div class="def" style="padding-top:14px">The evidence to support the claim</div></div>
  </div>
  <footer class="footer"><span class="url">www.summitadvisory.com</span><span class="band">Copyright @Summit Advisory 2024</span><span class="page">14</span></footer>
</section>

<!-- 15 -->
<section class="slide">
  <h2 class="title" style="left:29px;top:21px">Asking questions exercise</h2>
  <div class="brand"><span class="dot"></span>Summit Advisory</div>
  <p class="intro">We know that clients/educators <b>buy on <u>emotion</u> and justify with <u>logic</u></b>.<br>If we can uncover both sides of their needs then we have a distinct advantage.<br>Add to each side of the worksheet, the potential needs you might uncover<br>when asking your buyers early discovery questions.</p>
  <table class="grid-table needs">
    <tr><th>Emotional Needs (Personally orientated)</th><th>Financial Needs (Business oriented)</th></tr>
    <tr><td>Effort required to juggle rosters</td><td>Cost per day for an educator</td></tr>
    <tr><td>Hassle involved with change of suppliers</td><td>Maximising return per day for being an educator</td></tr>
    <tr><td>Personal preference for suppliers or consultants</td><td>Attracting new admissions (business growth)</td></tr>
    <tr><td>Fear of missing out</td><td>Managing to a budget</td></tr>
    <tr class="gap"><td></td><td></td></tr>
    <tr class="blank"><td></td><td></td></tr>
    <tr class="gap"><td></td><td></td></tr>
    <tr class="blank"><td></td><td></td></tr>
    <tr class="gap"><td></td><td></td></tr>
    <tr class="blank"><td></td><td></td></tr>
  </table>
  <footer class="footer"><span class="url">www.summitadvisory.com</span><span class="band">Copyright @Summit Advisory 2024</span><span class="page">15</span></footer>
</section>

<!-- 16 -->
<section class="slide">
  <h2 class="title" style="left:25px;top:25px">What is High-Performance BD:</h2>
  <div class="brand"><span class="dot"></span>Summit Advisory</div>
  <div class="hp">
    <div class="head">High Performance Positioning</div><div class="head">The Tavora Value Proposition</div>
    <div class="area"></div><div class="area"></div>
    <div class="head">Your Distinguishing Capabilities</div><div class="head">High Performance Results</div>
    <div class="area tall"></div><div class="area tall"></div>
  </div>
  <footer class="footer"><span class="url">www.summitadvisory.com</span><span class="band">Copyright @Summit Advisory 2024</span><span class="page">16</span></footer>
</section>

<!-- 17 -->
<section class="slide row2">
  <h2 class="title" style="left:24px;top:29px">Exercise Two: 2. Strategic opportunities</h2>
  <div class="brand"><span class="dot"></span>Summit Advisory</div>
  <p class="sub" style="left:27px;top:52px">Where are the biggest strategic opportunities for you?</p>
  <table class="grid-table strat">
    <colgroup><col style="width:93px"><col style="width:106px"><col></colgroup>
    <tr><th>Strategic dimension</th><th>Opportunity</th><th>How to convert the opportunity</th></tr>
    <tr><td class="dim"></td><td></td><td></td></tr>
    <tr><td class="dim"></td><td></td><td></td></tr>
    <tr><td class="dim"></td><td></td><td></td></tr>
    <tr><td class="dim"></td><td></td><td></td></tr>
    <tr><td class="dim"></td><td></td><td></td></tr>
    <tr><td class="dim"></td><td></td><td></td></tr>
    <tr><td class="dim"></td><td></td><td></td></tr>
  </table>
  <footer class="footer"><span class="url">www.summitadvisory.com</span><span class="band">Copyright @Summit Advisory 2024</span><span class="page">17</span></footer>
</section>

<!-- 18 -->
<section class="slide row2">
  <h2 class="title" style="left:29px;top:28px">Why Buyers Object</h2>
  <div class="brand"><span class="dot"></span>Summit Advisory</div>
  <table class="grid-table obj">
    <colgroup><col style="width:152px"><col style="width:112px"><col></colgroup>
    <tr><th>What they say</th><th>What this indicates</th><th>Objection type</th></tr>
    <tr><td>“That's a big claim. Really?”</td><td>Don't believe you</td><td class="type">Scepticism</td></tr>
    <tr><td>“No thanks, I already have a supplier for filling staff roles.”</td><td>Not interested enough</td><td class="type">Indifference</td></tr>
    <tr><td>“I have heard your name mentioned but we feel we are too small to use a recruitment service for our little centre up here.”</td><td>Unclear of the positive outcome</td><td class="type">Misunderstanding</td></tr>
    <tr><td>“No, I'm not that keen. But if you were to sharpen your pencil on rates, we might be more open to talk with you more.”</td><td>Testing your willingness to deal</td><td class="type">Try on</td></tr>
    <tr><td>“You simply cost more than the opposition in cost per head per day, and things are really tight for us right now.”</td><td>A deficiency in our offer</td><td class="type">Real</td></tr>
  </table>
  <footer class="footer"><span class="url">www.summitadvisory.com</span><span class="band">Copyright @Summit Advisory 2024</span><span class="page">18</span></footer>
</section>

<!-- 19 -->
<section class="slide row2">
  <h2 class="title" style="left:21px;top:35px;font-weight:700">SPACER – expressing benefits in single words</h2>
  <div class="brand"><span class="dot"></span>Summit Advisory</div>
  <p class="spacer-sub">All benefits derive from <b>one of these six power words</b>:</p>
  <div class="spacer">
    <div class="item"><div class="word"><b>S</b>afety</div><div class="text"><span>We have the highest screening, interviewing and ongoing educator management systems in the industry giving you <b>added peace of mind</b> for the right fit to role</span></div></div>
    <div class="item"><div class="word"><b>P</b>erformance</div><div class="text"><span>Our consultants go the extra distance in contacting, reporting and visiting your site to give you the very best experience when you need <b>to find relief educators</b></span></div></div>
    <div class="item"><div class="word"><b>A</b>ppearance</div><div class="text"><span>The QuickShift app gives you <b>full transparency</b> to your orders, both past, current and future in an easy to navigate online platform that shows all the information</span></div></div>
    <div class="item"><div class="word"><b>C</b>onvenience</div><div class="text"><span>Our consultants are available from 6.30am every day to manage those emergency situations where you need staff cover that day. We <b>make it easy</b> to get help.</span></div></div>
    <div class="item"><div class="word"><b>E</b>conomy</div><div class="text"><span>Our real value is that you get the right educator, in the right place, at the right time – all with <b>market competitive rates</b></span></div></div>
    <div class="item"><div class="word"><b>R</b>eliability</div><div class="text"><span>As the largest player in the market, you can rest assured that you are dealing with the <b>most professional consultants</b> with the largest network to pull from.</span></div></div>
  </div>
  <footer class="footer"><span class="url">www.summitadvisory.com</span><span class="band">Copyright @Summit Advisory 2024</span><span class="page">19</span></footer>
</section>

<!-- 20 -->
<section class="slide row3">
  <h2 class="title" style="left:30px;top:28px"><span style="margin-left:18px">Behaviours &amp; Culture</span></h2>
  <div class="brand" style="top:11px;right:16px"><span class="dot"></span>Summit Advisory</div>
  <table class="grid-table beh">
    <colgroup><col style="width:89px"><col style="width:56px"><col></colgroup>
    <tr><th>Objective</th><th>Practices</th><th>On Track</th></tr>
    <tr style="height:42px"><td class="obj-cell" rowspan="3">To ensure that our company values and virtues are turning up. We want our people to not just know but to live, embody and model these in both internal and external exchanges.</td><td class="prac">1. Lives our values</td><td><ul><li>Has been exposed to our company values and educated in their importance</li><li>Can state all seven of the CORE values</li><li>Knows what needs to turn up to demonstrate that each value is being lived</li><li>Examples of living the values are noted and discussed during each coaching session</li></ul></td></tr>
    <tr style="height:47px"><td class="prac">2. Embodies our virtues</td><td><ul><li>Can state WHY we have virtues that run beside our values</li><li>Knows the seven virtues and can list them accurately</li><li>Can show evidence of the virtues being embodied by the consultant during coaching sessions from real world application</li></ul></td></tr>
    <tr style="height:59px"><td class="prac">3. Safe Practices and Inclusion</td><td><ul><li>Is aware of the Tavora expectations of operating safely when at work</li><li>Evidence exists of safe use of motor vehicle</li><li>Has a clean and safe work environment with respect to electronic equipment, power connections, ergonomics and healthy work habits</li><li>Is aware of our inclusion policies to other team members</li><li>Can show evidence of championing our inclusion practices on the job when in a coaching session with their manager</li></ul></td></tr>
  </table>
  <footer class="footer"><span class="url">www.summitadvisory.com</span><span class="band">Copyright @Summit Advisory 2024</span><span class="page">20</span></footer>
</section>

<!-- 21 -->
<section class="slide row3">
  <h2 class="title" style="left:33px;top:24px">3. Opportunity Matrix – Client example</h2>
  <div class="brand" style="top:13px;right:16px"><span class="dot"></span>Summit Advisory</div>
  <span class="axis on" style="left:100px;top:50px">Existing Clients/Educators</span>
  <span class="axis off" style="left:237px;top:50px">New Clients/Educators</span>
  <span class="axis off" style="left:32px;top:89px;line-height:1.35">Additional<br>Services</span>
  <span class="axis on" style="left:32px;top:180px">Existing Services</span>
  <div class="matrix">
    <div class="quad"><h4>2. Client development<br>(Portfolio expansion)</h4><p>Offering <i>additional</i> service ranging to existing customers</p><ul><li>“Appropriate” service expansion</li><li>Proactive offers</li><li>Present new service innovations</li><li>Minimise competitors</li></ul></div>
    <div class="quad"><h4>4. Market development<br>(Infiltration)</h4><p>Offering <i>new</i> services/programs to <i>new</i> clients</p><ul><li>Niche marketing</li><li>Special service or program development</li></ul></div>
    <div class="quad"><h4>1. Client service<br>(Protection)</h4><p>Ensure existing Tavora clients continue to book with us</p><ul><li>Responsive contact</li><li>High quality service delivery</li><li>Frictionless account administration</li><li>Relationship enhancements</li></ul></div>
    <div class="quad"><h4>3. Market expansion<br>(Penetration)</h4><p>Offering existing services to <i>new</i> clients</p><ul><li>Targeted new business development</li><li>Convert inquiries as new business</li><li>Reinstate lapsed clients</li><li>Expand within groups or networks</li></ul></div>
  </div>
  <svg class="zig" width="56" height="24" viewBox="0 0 56 24"><polyline points="1,22 21,2 39,20 52,4" fill="none" stroke="#2f8fd8" stroke-width="1.6"/></svg>
  <footer class="footer"><span class="url">www.summitadvisory.com</span><span class="band">Copyright @Summit Advisory 2024</span><span class="page">21</span></footer>
</section>

<!-- 22 -->
<section class="slide row3">
  <h2 class="title" style="left:25px;top:21px">Coaching to GROW</h2>
  <div class="brand" style="top:14px;right:16px"><span class="dot"></span>Summit Advisory</div>
  <span class="grow-label" style="left:27px;top:40px;color:var(--blue);font-style:italic">Before coaching session</span>
  <svg class="grow-shape" width="72" height="192" viewBox="0 0 72 192">
    <polygon points="0,0 72,0 72,170 36,191 0,170" fill="#232a63"/>
    <polygon points="0,22 36,49 72,22 72,95 36,122 0,95" fill="#69b4e6"/>
  </svg>
  <div class="grow-label" style="left:30px;top:56px;color:#fff;font-size:4.4px"><b>Before Coaching:</b><br>☐ Schedule<br>☐ Prepare &amp; plan</div>
  <div class="grow-label" style="left:29px;top:104px;color:var(--navy);font-size:4.4px;font-style:italic"><b>During Coaching: GROW</b><br>&nbsp;&nbsp;• &nbsp;&nbsp;&nbsp;OALS<br>&nbsp;&nbsp;• &nbsp;&nbsp;&nbsp;EALITIES<br>&nbsp;&nbsp;• &nbsp;&nbsp;&nbsp;PTIONS<br>&nbsp;&nbsp;• &nbsp;&nbsp;&nbsp;&nbsp;ILL TO ACT</div>
  <div class="grow-label" style="left:28px;top:178px;color:#fff;font-size:4.4px;font-style:italic"><b>Follow-up:</b><br>• Measure<br>• Observe<br>• Feedback &amp; encouragement<br>• Further coaching</div>
  <div class="col" style="left:100px;top:40px;width:137px">
    <h5>During Coaching Session:</h5>
    <div class="block" style="height:32px"><ol><li class="lead">GOALS</li></ol><ul><li>Agree purpose/agenda of the session</li><li>Check understanding of relevant goals, targets or standards</li></ul></div>
    <div class="block" style="height:40px"><ol start="2"><li class="lead">REALITIES</li></ol><ul><li>Ask first! – Ask team member how they feel they have performed or what they have experienced and why</li><li>Share your thoughts and clarify any perception gaps</li></ul></div>
    <div class="block" style="height:60px"><ol start="3"><li class="lead">OPTIONS</li></ol><ul><li>Ask what can be done differently / reinforce the positives</li><li>Generate joint ownership of the problem</li><li>Uncover obstacles and issues</li><li>Use a systematic approach to problem solving</li><li>Offer information and assistance</li></ul></div>
    <div class="block" style="height:56px"><ol start="4"><li class="lead">WILL TO ACT</li></ol><ul><li>Check for commitment to improvements</li><li>Express confidence and offer support</li><li>Summarise the key action steps mutually agreed upon and ensure they are documented</li><li>Add any other considerations you can offer</li><li>Finish on a positive note</li></ul></div>
  </div>
  <div class="col" style="left:239px;top:40px;width:134px">
    <h5>Possible Questions to Ask:</h5>
    <div class="block" style="height:32px"><ul class="q"><li>“Let's remind ourselves what we're trying to achieve…”</li><li>What do we want to get out of this session?</li><li>What would be ideal for you in future?</li></ul></div>
    <div class="block" style="height:40px"><b>Ask the person how they think things are now</b><ul class="q"><li>What do you think of your current performance?</li><li>What did you do well? What worked for you?</li><li>What didn't &amp; why?</li><li>What did you learn?</li></ul></div>
    <div class="block" style="height:60px"><b>Ask the person what they learned from the experience</b><ul class="q"><li>What would you do differently next time?</li><li>What could you improve on?</li></ul><b>Share your observations</b><ul class="q"><li>Things I thought you did well were…</li><li>Things you could try and do differently are…</li></ul></div>
    <div class="block" style="height:56px"><b>Agree actions going forward</b><ul class="q"><li>Let's agree one or two things you'll aim to achieve within an agreed timeframe</li><li>Discuss support mechanism/ assistance, where appropriate</li></ul></div>
  </div>
  <footer class="footer"><span class="url">www.summitadvisory.com</span><span class="band">Copyright @Summit Advisory 2024</span><span class="page">22</span></footer>
</section>

</main>
</body>
</html>
```